Terra Swift Business Card Design

We need to improve the design of our current business card. We are a erosion control, hydro seeding company that serves many markets. We are attaching the current business card and our logo as reference. You may also visit our site at www.terraswiftllc.example to reference.

```html
<!DOCTYPE html>
<html lang="en">
<head>
<meta charset="utf-8">
<title>Terra Swift Business Card</title>
<link href="https://fonts.googleapis.com/css2?family=Open+Sans:wght@400;600;700;800&display=swap" rel="stylesheet">
<style>
  :root {
    --page-bg: #2b2b2b;
    --card-bg: #ffffff;
    --green-dark: #0b6b3a;
    --green-bright: #1bb172;
    --text-main: #333333;
    --text-dark: #1e1e1e;
    --watermark: #f0f0ee;
  }
  * { margin: 0; padding: 0; box-sizing: border-box; }
  html, body {
    width: 1200px; height: 1059px; overflow: hidden;
    background: var(--page-bg);
    font-family: "Open Sans", Arial, sans-serif;
  }
  .canvas { position: relative; width: 1200px; height: 1059px; }
  .card {
    position: absolute;
    background: var(--card-bg);
    border-radius: 24px;
    overflow: hidden;
    box-shadow: 0 8px 24px rgba(0,0,0,0.45);
  }
  .card-front { left: 256px; top: 88px; width: 688px; height: 391px; }
  .card-back  { left: 252px; top: 546px; width: 696px; height: 395px; }

  .brand-name {
    color: var(--green-dark);
    font-weight: 800;
    white-space: nowrap;
    letter-spacing: -0.5px;
  }
  .card-front .brand-name { position: absolute; left: 25px; top: 24px; font-size: 33px; }
  .card-back .brand-name {
    position: absolute; left: 0; right: 0; top: 168px;
    text-align: center; font-size: 54px; line-height: 60px;
  }

  .watermark-disc {
    position: absolute; left: 330px; top: 52px;
    width: 300px; height: 300px; border-radius: 50%;
    background: var(--watermark);
  }

  .address {
    position: absolute; left: 25px; top: 157px;
    font-size: 18px; line-height: 24.5px; color: var(--text-main);
  }
  .contacts {
    position: absolute; left: 25px; top: 270px;
    list-style: none; font-size: 18px; line-height: 24.5px; color: var(--text-main);
  }
  .contacts li { display: flex; align-items: center; gap: 7px; }
  .contacts svg { width: 16px; height: 16px; flex: none; fill: var(--green-dark); }

  .person {
    position: absolute; right: 22px; top: 165px; text-align: right;
  }
  .person-name {
    font-size: 27px; font-weight: 600; line-height: 32px;
    color: var(--green-dark); letter-spacing: 0.3px;
  }
  .person-name .surname { color: var(--green-bright); }
  .person-title { font-size: 18.5px; color: var(--text-dark); line-height: 26px; }
  .accent-bar {
    position: absolute; right: 0; top: 171px;
    width: 10px; height: 51px; background: var(--green-bright);
  }
</style>
</head>
<body>
<div class="canvas">

  <section class="card card-front">
    <div class="watermark-disc"></div>
    <div class="brand-name">Terra Swift Solutions</div>

    <address class="address" style="font-style:normal">
      Corporate Headquarters<br>
      275 Willow Bend Road<br>
      Riverton, NC 28401
    </address>

    <ul class="contacts">
      <li>
        <svg viewBox="0 0 16 16" aria-hidden="true"><path d="M3.5 1.5l2.3 0 1 3.2-1.6 1.3a8 8 0 0 0 4.8 4.8l1.3-1.6 3.2 1v2.3c0 .8-.7 1.5-1.5 1.5C7.3 14 2 8.7 2 3c0-.8.7-1.5 1.5-1.5z"/></svg>
        (555) 014-2270
      </li>
      <li>
        <svg viewBox="0 0 16 16" aria-hidden="true"><path d="M1 4h3v11H1zM5 2h7l2 2v11H5zM7 7h2v2H7zm3 0h2v2h-2zm-3 3h2v2H7zm3 0h2v2h-2z"/></svg>
        (555) 014-2271
      </li>
      <li>
        <svg viewBox="0 0 16 16" aria-hidden="true"><path d="M1 6l7-5 7 5v9H1zm2 1.2V13h10V7.2L8 10.5z"/></svg>
        info@terraswiftllc.example
      </li>
      <li>
        <svg viewBox="0 0 16 16" aria-hidden="true"><circle cx="8" cy="8" r="7"/><path d="M4 4c2 0 2 2 4 2s1 3-1 3-1 3-3 2c-1-2 0-3-1-4z M10 10c1 0 2 1 2 2-1 1-2 1-2-2z" fill="#ffffff"/></svg>
        www.terraswiftllc.example
      </li>
    </ul>

    <div class="person">
      <div class="person-name">DANIEL <span class="surname">REYES</span></div>
      <div class="person-title">Managing Director</div>
    </div>
    <div class="accent-bar"></div>
  </section>

  <section class="card card-back">
    <div class="brand-name">Terra Swift Solutions</div>
  </section>

</div>
</body>
</html>
```